KPR Business Advisors Corporate Stationery

A Corporate Stationery Design is required for KPR Business Advisors - Chartered Accountants. The Design is to incorporate Black and Navy Blue and is to give an example of the following: Letterhead/DL Envelope/With Compliment Slip/Business Card and Binding Covers.

Industry/Entity Type

Business

Requirements
Must have
• The Corporate Stationery has the following compulsory attributes:

Logo (Refer File) - words underneath Chartered Accountants
ABN 41 302 775 918
Street Address: Level 4/28 Marlowe St Melbourne VIC
Postal Address: PO Box 27391 Fenwick Rd North Melbourne VIC 8003
Telephone: 03 9487 2236
Facsimile: 03 9487 2290
Directors: Doug Pellamy Ken Abarra Rosalie Finch

```html
<!DOCTYPE html>
<html lang="en">
<head>
<meta charset="utf-8">
<title>KPR Business Advisors – Corporate Stationery</title>
<link href="https://fonts.googleapis.com/css2?family=Mulish:wght@400;700&display=swap" rel="stylesheet">
<style>
  :root {
    --navy: #2a3192;
    --navy-deep: #1d2a8a;
    --royal: #2d6fd6;
    --black: #231f20;
    --ink: #3a3a3a;
    --paper: #ffffff;
    --backdrop: #5a5a5a;
  }
  * { box-sizing: border-box; margin: 0; padding: 0; }
  html, body { width: 1200px; height: 849px; overflow: hidden; }
  body {
    position: relative;
    background: var(--backdrop);
    font-family: "Mulish", "Century Gothic", sans-serif;
    color: var(--ink);
  }
  .sheet {
    position: absolute;
    background: var(--paper);
    box-shadow: 2px 3px 8px rgba(0,0,0,.45);
  }

  /* Footer band: plain navy and black blocks */
  .band { position: absolute; left: 0; width: 100%; display: flex; }
  .band__navy { background: var(--navy); height: 100%; }
  .band__black { background: var(--black); height: 100%; flex: 1; }

  /* Brand lockup */
  .brand { position: absolute; display: flex; align-items: flex-start; }
  .brand__square { background: var(--navy); flex: none; }
  .brand__text { line-height: 1; }
  .brand__name { color: var(--navy); display: block; font-weight: 700; letter-spacing: .3px; }
  .brand__line { color: var(--black); display: block; font-weight: 400; }

  .address strong { color: var(--navy); font-weight: 700; }
  .address .sep { color: var(--black); margin: 0 5px; font-weight: 700; }

  /* Letterhead */
  .letterhead { left: 46px; top: 40px; width: 596px; height: 770px; }
  .letterhead .brand { left: 39px; top: 38px; }
  .letterhead .brand__square { width: 47px; height: 47px; margin-right: 10px; }
  .letterhead .brand__name { font-size: 25px; margin-bottom: 3px; }
  .letterhead .brand__line { font-size: 11px; line-height: 11.5px; }
  .letterhead .address {
    position: absolute; right: 39px; top: 707px;
    font-size: 8.6px; line-height: 10.4px; text-align: right;
  }
  .letterhead .band { bottom: 0; height: 8px; }
  .letterhead .band__navy { width: 376px; }

  /* Business card front */
  .card-front { left: 558px; top: 135px; width: 244px; height: 137px; }
  .card-front .brand { left: 14px; top: 15px; }
  .card-front .brand__square { width: 32px; height: 32px; margin-right: 7px; }
  .card-front .brand__name { font-size: 17px; margin-bottom: 1px; }
  .card-front .brand__line { font-size: 7.2px; line-height: 7.8px; }
  .card-front .address {
    position: absolute; left: 14px; top: 97px;
    font-size: 5px; line-height: 6.6px;
  }
  .card-front .person { position: absolute; left: 151px; top: 92px; line-height: 1; }
  .person__name { color: var(--navy); font-size: 9.5px; font-weight: 700; display: block; margin-bottom: 2px; }
  .person__role { color: var(--ink); font-size: 7px; display: block; }
  .card-front .band { bottom: 0; height: 4px; }
  .card-front .band__navy { width: 146px; }

  /* Business card back */
  .card-back {
    left: 843px; top: 135px; width: 245px; height: 140px;
    background: radial-gradient(ellipse at 50% 40%, var(--royal) 0%, var(--navy-deep) 80%);
  }
  .card-back .brand { left: 59px; top: 53px; }
  .card-back .brand__square { width: 34px; height: 34px; margin-right: 6px; background: var(--paper); }
  .card-back .brand__name, .card-back .brand__line { color: var(--paper); }
  .card-back .brand__name { font-size: 17px; margin-bottom: 1px; }
  .card-back .brand__line { font-size: 7.2px; line-height: 7.8px; }

  /* DL envelope */
  .envelope__flap {
    position: absolute; left: 490px; top: 308px; width: 665px; height: 118px;
    border-radius: 14px 14px 0 0;
    background: radial-gradient(ellipse at 50% 60%, var(--royal) 0%, var(--navy-deep) 75%);
    box-shadow: 2px 2px 6px rgba(0,0,0,.35);
  }
  .envelope__flap .brand { left: 276px; top: 46px; transform: rotate(180deg); }
  .envelope__flap .brand__square { width: 30px; height: 30px; margin-right: 6px; background: var(--paper); }
  .envelope__flap .brand__name, .envelope__flap .brand__line { color: var(--paper); }
  .envelope__flap .brand__name { font-size: 16px; margin-bottom: 1px; }
  .envelope__flap .brand__line { font-size: 6.8px; line-height: 7.2px; }

  .envelope { left: 490px; top: 425px; width: 665px; height: 290px; }
  .envelope .brand { left: 31px; top: 32px; }
  .envelope .brand__square { width: 47px; height: 47px; margin-right: 10px; }
  .envelope .brand__name { font-size: 25px; margin-bottom: 3px; }
  .envelope .brand__line { font-size: 11px; line-height: 11.5px; }
  .envelope .address {
    position: absolute; left: 31px; top: 100px;
    font-size: 8.6px; line-height: 10.4px;
  }
  .envelope .band { bottom: 0; height: 8px; }
  .envelope .band__navy { width: 536px; }
</style>
</head>
<body>

<section class="sheet letterhead">
  <div class="brand">
    <span class="brand__square"></span>
    <div class="brand__text">
      <span class="brand__name">KPR</span>
      <span class="brand__line">Business Advisors Pty Ltd</span>
      <span class="brand__line">Chartered Accountants</span>
    </div>
  </div>
  <p class="address">
    Level 4/28 Marlowe St Melbourne VIC<br>
    PO Box 27391 Fenwick Rd North Melbourne VIC 8003<br>
    <strong>Tel :</strong> 03 9487 2236<span class="sep">|</span><strong>Fax :</strong> 03 9487 2290<br>
    ABN 41 302 775 918
  </p>
  <div class="band" aria-hidden="true"><span class="band__navy"></span><span class="band__black"></span></div>
</section>

<section class="sheet card-front">
  <div class="brand">
    <span class="brand__square"></span>
    <div class="brand__text">
      <span class="brand__name">KPR</span>
      <span class="brand__line">Business Advisors Pty Ltd</span>
      <span class="brand__line">Chartered Accountants</span>
    </div>
  </div>
  <p class="address">
    Level 4/28 Marlowe St Melbourne VIC<br>
    PO Box 27391 Fenwick Rd North Melbourne VIC 8003<br>
    <strong>Tel</strong> &nbsp;: 03 9487 2236<br>
    <strong>Fax</strong> : 03 9487 2290<br>
    ABN 41 302 775 918
  </p>
  <div class="person">
    <span class="person__name">Doug Pellamy</span>
    <span class="person__role">Director</span>
  </div>
  <div class="band" aria-hidden="true"><span class="band__navy"></span><span class="band__black"></span></div>
</section>

<section class="sheet card-back">
  <div class="brand">
    <span class="brand__square"></span>
    <div class="brand__text">
      <span class="brand__name">KPR</span>
      <span class="brand__line">Business Advisors Pty Ltd</span>
      <span class="brand__line">Chartered Accountants</span>
    </div>
  </div>
</section>

<section class="envelope__flap">
  <div class="brand">
    <span class="brand__square"></span>
    <div class="brand__text">
      <span class="brand__name">KPR</span>
      <span class="brand__line">Business Advisors Pty Ltd</span>
      <span class="brand__line">Chartered Accountants</span>
    </div>
  </div>
</section>
<section class="sheet envelope">
  <div class="brand">
    <span class="brand__square"></span>
    <div class="brand__text">
      <span class="brand__name">KPR</span>
      <span class="brand__line">Business Advisors Pty Ltd</span>
      <span class="brand__line">Chartered Accountants</span>
    </div>
  </div>
  <p class="address">
    Level 4/28 Marlowe St Melbourne VIC<br>
    PO Box 27391 Fenwick Rd North Melbourne VIC 8003<br>
    <strong>Tel :</strong> 03 9487 2236<span class="sep">|</span><strong>Fax :</strong> 03 9487 2290<br>
    ABN 41 302 775 918
  </p>
  <div class="band" aria-hidden="true"><span class="band__navy"></span><span class="band__black"></span></div>
</section>

</body>
</html>
```